Calm and Compass Health Flyer (new business startup)

One page...clear enough to be read if faxed. This mental health clinic treats depression/anxiety in kids and adults. It also treats opiate and alcohol addiction. It's in downtown Harlow Falls, NY and the owner of the clinic is from Harlow Falls NY, where it's located. This clinic does not take health insurance, so it charges a low rate of $75 a visit once they pay the $125 starting fee.

Target Market(s)

doctors offices, new patients

Industry/Entity Type

Doctor

Requirements
Must have
• see microsoft word document. pdf is printed on the company letterhead.
Nice to have
• a simplified map would be nice. if you can include the building it would be a plus. The same two fonts were used in the business cards and letter head (kennedy small caps boo*) and Refrigerator Delux.

```html
<!DOCTYPE html>
<html lang="en">
<head>
<meta charset="utf-8">
<title>Calm and Compass Health Flyer</title>
<link rel="stylesheet" href="https://fonts.googleapis.com/css2?family=Crimson+Pro:wght@400;500&family=Montserrat:wght@700&family=Oswald:wght@400;500;600&display=swap">
<style>
  :root {
    --orange: #ee7232;
    --orange-deep: #e8622a;
    --orange-light: #f4a06a;
    --blue: #27a5df;
    --blue-title: #2a9fd8;
    --ink: #3a3a3a;
    --paper: #ffffff;
    --page-bg: #f2f2f2;
  }
  * { box-sizing: border-box; margin: 0; padding: 0; }
  html, body { width: 1200px; height: 1200px; overflow: hidden; background: var(--page-bg); }
  .flyer {
    position: absolute; left: 205px; top: 40px;
    width: 790px; height: 1120px; background: var(--paper);
    overflow: hidden;
  }
  /* Header */
  .header { position: absolute; left: 0; top: 0; width: 100%; height: 184px; display: flex; align-items: center; justify-content: center; }
  .header__name { font-family: "Montserrat", sans-serif; font-weight: 700; font-size: 37px; color: var(--orange); letter-spacing: -0.5px; }
  /* Orange band */
  .hero { position: absolute; left: 0; top: 184px; width: 100%; height: 496px;
    background: radial-gradient(ellipse at 62% 48%, var(--orange-light) 0%, var(--orange) 55%, var(--orange-deep) 100%); }
  .hero__photo { position: absolute; left: 0; top: -10px; width: 250px; height: 506px;
    background: linear-gradient(180deg, #e9e4e0 0%, #f4f4f4 45%, #d7e6e6 100%); }
  .hero__text { position: absolute; left: 284px; right: 40px; color: #fff; font-family: "Crimson Pro", serif; }
  .hours { top: 44px; left: 292px; font-size: 39px; line-height: 41px; font-weight: 500; }
  .services { top: 254px; font-size: 33px; line-height: 38px; font-weight: 500; }
  .services__item { margin-bottom: 8px; }
  .services__line { display: flex; align-items: baseline; }
  .services__dots { flex: 1; border-bottom: 3px dotted #fff; margin: 0 4px 8px; }
  .ages { top: 440px; font-size: 32px; font-weight: 400; }
  /* Lower section */
  .lower { position: absolute; left: 0; top: 680px; width: 100%; height: 333px;
    background: linear-gradient(90deg, #f3f2f1 0%, #e7e3df 60%, #ddd8d3 100%); }
  .lower__map { position: absolute; left: 62px; top: 10px; width: 270px; height: 270px; border-radius: 50%;
    border: 3px solid var(--orange); background: linear-gradient(160deg, #eeeeee 0%, #e2e2e2 60%, #cfe3ee 100%); }
  .lower__building { position: absolute; left: 12px; top: 95px; width: 135px; height: 75px;
    background: linear-gradient(180deg, #6d4a3c 0%, #4f3a32 100%); }
  .conditions { position: absolute; left: 380px; top: 12px; font-family: "Oswald", sans-serif; color: var(--ink); }
  .conditions__title { font-weight: 600; font-size: 33px; color: var(--blue-title); letter-spacing: 0.3px; }
  .conditions__cols { display: flex; gap: 40px; margin-top: 6px; }
  .conditions__list { list-style: none; font-size: 26px; line-height: 39px; }
  .conditions__list li { position: relative; padding-left: 24px; }
  .conditions__list li::before { content: ""; position: absolute; left: 2px; top: 16px; width: 9px; height: 9px; border-radius: 50%; background: var(--ink); }
  .conditions__list .two-line { line-height: 32px; padding-top: 4px; }
  .tagline { position: absolute; left: 390px; top: 258px; font-family: "Oswald", sans-serif; font-style: italic; font-size: 19px; color: var(--orange); }
  .note { position: absolute; left: 30px; right: 30px; top: 286px; text-align: center; font-family: "Oswald", sans-serif; font-size: 14.5px; line-height: 22px; color: var(--ink); }
  /* Footer */
  .footer { position: absolute; left: 0; top: 1013px; width: 100%; height: 107px; background: var(--blue);
    color: #fff; font-family: "Oswald", sans-serif; font-size: 20px; }
  .footer__address { position: absolute; left: 38px; top: 14px; line-height: 29px; }
  .footer__contact { position: absolute; right: 36px; top: 6px; text-align: right; line-height: 29px; }
</style>
</head>
<body>
<main class="flyer">
  <header class="header">
    <h1 class="header__name">CALM AND COMPASS HEALTH</h1>
  </header>

  <section class="hero">
    <div class="hero__photo" role="img" aria-label="Photo of a doctor in a white coat with stethoscope holding a clipboard"></div>
    <div class="hero__text hours">HOURS:<br>Monday and Saturdays<br>9-4pm</div>
    <div class="hero__text services">
      <div class="services__item">Psychiatric Evaluation
        <div class="services__line"><span>(45min)</span><span class="services__dots"></span><span>$125*</span></div></div>
      <div class="services__item">Psychiatric Office Visit
        <div class="services__line"><span>(15min)</span><span class="services__dots"></span><span>$75*</span></div></div>
    </div>
    <div class="hero__text ages">AGES:&nbsp; 6 YEARS OLD AND UP</div>
  </section>

  <section class="lower" role="img" aria-label="Faded photo of downtown brick buildings">
    <div class="lower__map" role="img" aria-label="Street map of the downtown area with the clinic location pinned"></div>
    <div class="lower__building" role="img" aria-label="Photo of the clinic's brick building"></div>
    <div class="conditions">
      <h2 class="conditions__title">Conditions Treated:</h2>
      <div class="conditions__cols">
        <ul class="conditions__list">
          <li>Depression</li>
          <li>PTSD</li>
          <li>Addiction</li>
          <li class="two-line">Childhood Mood<br>Disorders</li>
        </ul>
        <ul class="conditions__list">
          <li>Anxiety</li>
          <li>ADHD</li>
          <li>Bipolar</li>
        </ul>
      </div>
    </div>
    <p class="tagline">“We work for you, not the insurance companies”</p>
    <p class="note">*Although we do not partner with any Health Insurance Companies at this time, a bill will be provided to you at the<br>time of service for you to submit to your insurance company.</p>
  </section>

  <footer class="footer">
    <div class="footer__address">240 W. Water #118 Harlow Falls, NY 12990<br>With Dr. Helen Varrow</div>
    <div class="footer__contact">(P) 555 014-2210<br>(F) 555 018-7730<br>www.calm-compass.com</div>
  </footer>
</main>
</body>
</html>
```